Solution Matrix for our Company

Develop an image that describes our "4 solutions". We eventually will list the products and services we have that address the solution being discussed. Our main website is http://brightlane4jobs.example/. Feel free to look through the material there as well as the material we are addressing.

The mock document is a summary of the 4 solution buckets. We have also attached some samples from states that have done similar work. Feel free to be creative and use graphics and/or pictures in your design

Target Market(s)

Education

```html
<!DOCTYPE html>
<html lang="en">
<head>
<meta charset="utf-8">
<title>BL4J Career Readiness Model</title>
<link href="https://fonts.googleapis.com/css2?family=Roboto:wght@400;500;700&display=swap" rel="stylesheet">
<style>
  :root {
    --ink: #2f4553;
    --blue: #0aa0d6;
    --orange: #ff6f00;
    --teal: #52dcb8;
    --slate: #2f4553;
    --white: #ffffff;
    --text-dark: #2a2a2a;
  }
  html, body { margin: 0; padding: 0; overflow: hidden; }
  body { background: var(--white); font-family: "Roboto", Arial, sans-serif; }
  .canvas { position: relative; width: 1200px; height: 1000px; overflow: hidden; background: var(--white); }
  .wheel { position: absolute; left: 0; top: 0; }
  .model-title { position: absolute; left: 199px; top: 62px; color: var(--ink); margin: 0; }
  .model-title .brand { display: block; font-size: 40px; font-weight: 700; line-height: 46px; }
  .model-title .name { display: block; font-size: 28px; font-weight: 700; line-height: 33px; }
  .mission { position: absolute; left: 199px; top: 174px; margin: 0; font-size: 17px; line-height: 20px; color: var(--ink); }
  .segment-copy { position: absolute; color: var(--white); }
  .segment-copy p { margin: 0; }
  .segment-copy ul { margin: 0; padding-left: 32px; list-style: disc; }
  .copy-supported { left: 405px; top: 265px; width: 190px; font-size: 9.2px; line-height: 10.8px; }
  .copy-supported ul { margin-top: 10px; }
  .copy-prepared { left: 683px; top: 310px; width: 200px; font-size: 9.8px; line-height: 11.4px; }
  .copy-prepared ul { margin-top: 10px; padding-left: 42px; line-height: 12.4px; }
  .copy-wise { left: 650px; top: 688px; width: 180px; font-size: 10.6px; line-height: 13px; color: var(--ink); }
  .copy-wise ul { margin-top: 12px; padding-left: 30px; }
  .copy-engaged { left: 397px; top: 721px; width: 200px; font-size: 11.6px; line-height: 13.3px; }
  .copy-engaged ul { margin-top: 12px; padding-left: 28px; }
  .core { position: absolute; left: 492px; top: 455px; width: 210px; text-align: center; color: var(--text-dark); }
  .core h2 { margin: 0; font-size: 12.3px; font-weight: 700; line-height: 14px; }
  .core .sub { margin: 0 0 10px; font-size: 10.4px; line-height: 13px; }
  .core .body { margin: 0 0 10px; font-size: 10.4px; line-height: 12.2px; }
  .core h3 { margin: 0; font-size: 12.3px; font-weight: 700; line-height: 14px; }
  .core ul { margin: 0; padding-left: 36px; text-align: left; font-size: 10.4px; line-height: 12.2px; }
  .segment-label { font-family: "Roboto", Arial, sans-serif; font-weight: 700; font-size: 21px; fill: var(--white); letter-spacing: 0.3px; }
</style>
</head>
<body>
<div class="canvas">
  <svg class="wheel" width="1200" height="1000" viewBox="0 0 1200 1000" aria-hidden="false">
    <defs>
      <filter id="soft-shadow" x="-30%" y="-30%" width="160%" height="160%">
        <feDropShadow dx="0" dy="6" stdDeviation="12" flood-color="#000" flood-opacity="0.28"/>
      </filter>
      <filter id="core-shadow" x="-30%" y="-30%" width="160%" height="160%">
        <feDropShadow dx="0" dy="0" stdDeviation="9" flood-color="#000" flood-opacity="0.35"/>
      </filter>
      <path id="arc-supported" d="M -158.4 -22.3 A 160 160 0 0 1 -13.9 -159.4"/>
      <path id="arc-prepared" d="M 5.6 -159.9 A 160 160 0 0 1 156.5 -33.3"/>
      <path id="arc-wise" d="M 71 152.3 A 168 168 0 0 0 165.4 -29.2"/>
      <path id="arc-engaged" d="M -159.4 13.9 A 160 160 0 0 0 13.9 159.4"/>
    </defs>
    <g transform="translate(592 540)">
      <path class="segment-wise" fill="var(--teal)" filter="url(#soft-shadow)"
            d="M 331.3 -76.5 A 340 340 0 0 1 35.5 338.1 L 13.9 132.3 A 133 133 0 0 0 129.6 -29.9 Z"/>
      <path class="segment-engaged" fill="var(--slate)" filter="url(#soft-shadow)"
            d="M 36.4 346.1 A 348 348 0 0 1 -348 0 L -133 0 A 133 133 0 0 0 13.9 132.3 Z"/>
      <path class="segment-supported" fill="var(--blue)" filter="url(#soft-shadow)"
            d="M -345 0 A 345 345 0 0 1 30.1 -343.7 L 11.6 -132.5 A 133 133 0 0 0 -133 0 Z"/>
      <path class="segment-prepared" fill="var(--orange)" filter="url(#soft-shadow)"
            d="M 34 -388.5 A 390 390 0 0 1 380 -87.7 L 129.6 -29.9 A 133 133 0 0 0 11.6 -132.5 Z"/>
      <circle class="core-disc" r="133" fill="var(--white)" filter="url(#core-shadow)"/>

      <text class="segment-label"><textPath href="#arc-supported" startOffset="50%" text-anchor="middle">Career Supported</textPath></text>
      <text class="segment-label"><textPath href="#arc-prepared" startOffset="50%" text-anchor="middle">Career Prepared</textPath></text>
      <text class="segment-label"><textPath href="#arc-wise" startOffset="50%" text-anchor="middle">Career Wise</textPath></text>
      <text class="segment-label"><textPath href="#arc-engaged" startOffset="50%" text-anchor="middle">Career Engaged</textPath></text>
    </g>

    <!-- support agent icon area -->
    <rect class="icon-support" x="319" y="390" width="80" height="90" rx="36" fill="var(--white)" opacity="0.9"
          role="img" aria-label="Support agent with headset icon"/>

    <!-- document with download arrow -->
    <g class="icon-document" fill="none" stroke="var(--white)" stroke-width="6" stroke-linejoin="round" stroke-linecap="round">
      <path d="M 650 206 L 696 206 L 710 220 L 710 260 M 700 282 L 650 282 L 650 206"/>
      <line x1="662" y1="226" x2="694" y2="226"/>
      <line x1="662" y1="240" x2="696" y2="240"/>
      <line x1="662" y1="254" x2="696" y2="254"/>
      <line x1="662" y1="268" x2="688" y2="268"/>
      <line x1="712" y1="254" x2="712" y2="282"/>
      <path d="M 702 274 L 712 284 L 722 274"/>
    </g>

    <!-- lightbulb -->
    <g class="icon-bulb" fill="none" stroke="var(--white)" stroke-width="7" stroke-linecap="round" stroke-linejoin="round">
      <path d="M 838 600 C 822 582 816 566 818 548 C 822 525 838 514 856 514 C 874 514 890 525 893 548 C 896 566 889 582 873 600 L 872 612 L 840 612 Z"/>
      <path d="M 842 622 L 870 622 L 870 628 C 870 634 866 637 860 637 L 852 637 C 846 637 842 634 842 628 Z"/>
      <path d="M 844 570 L 851 562 L 856 568 L 861 562 L 868 570"/>
    </g>

    <!-- chat bubbles -->
    <g class="icon-chat">
      <path d="M 340 595 A 36 36 0 1 0 336 662 L 330 678 L 352 664" fill="none" stroke="var(--white)" stroke-width="8" stroke-linejoin="round"/>
      <circle cx="360" cy="616" r="32" fill="var(--white)"/>
      <path d="M 370 640 L 386 670 L 392 636 Z" fill="var(--white)"/>
      <circle cx="360" cy="616" r="24" fill="var(--slate)"/>
      <rect x="347" y="605" width="26" height="7" rx="3.5" fill="var(--white)"/>
      <rect x="347" y="619" width="26" height="7" rx="3.5" fill="var(--white)"/>
    </g>
  </svg>

  <h1 class="model-title"><span class="brand">BL4J</span><span class="name">Career Readiness<br>Model</span></h1>
  <p class="mission">Our mission is to ensure<br>all students are:</p>

  <div class="segment-copy copy-supported">
    <p>Students benefit from informed educational leadership and policymaking that result in effective career resources and learning opportunities.</p>
    <ul>
      <li>BL4J Policy Tools</li>
      <li>Federal CTE Grant Technical Support</li>
      <li>Professional Development</li>
      <li>Industry-Education Relationships</li>
    </ul>
  </div>

  <div class="segment-copy copy-prepared">
    <p>Students benefit from informed educational leadership and policymaking that result in effective career resources and learning opportunities.</p>
    <ul>
      <li>BL4J Policy Tools</li>
      <li>Federal CTE Grant Technical Support</li>
      <li>Professional Development</li>
      <li>Industry-Education Relationships</li>
    </ul>
  </div>

  <div class="segment-copy copy-wise">
    <p>Students have insight into personal values and interests, as well as the economic realities of the job market, that supports informed career decisions.</p>
    <ul>
      <li>Career Pathways</li>
      <li>Career Exploration</li>
      <li>Educator Career Guides</li>
    </ul>
  </div>

  <div class="segment-copy copy-engaged">
    <p>Students are motivated and inspired to develop career skills and seek employment opportunities that meet both personal and community needs.</p>
    <ul>
      <li>Career Awareness &amp; Exposure</li>
      <li>Purposeful Learning</li>
    </ul>
  </div>

  <div class="core">
    <h2>Data-Informed and</h2>
    <p class="sub">Evidence-Based Practices</p>
    <p class="body">BrightLane4Jobs relies on robust labor market data tools and sound educational research to guide our development efforts and encourage the use of informed career readiness practices educational settings.</p>
    <h3>BL4J Data Tools</h3>
    <ul>
      <li>Labor Market Data System</li>
      <li>Employer Surveys</li>
      <li>Regional Labor Market Reports</li>
    </ul>
  </div>
</div>
</body>
</html>
```